Update New Business Card - For Start Up

I need to update my business card, I have our old version for example. I would like to keep to the same colors and theme. We are a threat reporting and case management tool for corporations and educational institutions.

Target Market(s)

Corporate Security and Human Resources, School Administrators and Superintendents.

Industry/Entity Type

Physical Security and Technology.

Contact Information for Business Card

My Name, Founder/CEO, phone number 555-214-6082, Logo, Web...

Colors
0054AA
0677BA
7BADD7
CADEEF
E8F1F8

Requirements
Must have
• Something new and trendy.

```html
<!DOCTYPE html>
<html lang="en">
<head>
<meta charset="utf-8">
<title>Vantrel Business Card</title>
<link href="https://fonts.googleapis.com/css2?family=Montserrat:ital,wght@0,400;0,500;0,600;1,400&display=swap" rel="stylesheet">
<style>
  :root {
    --brand-deep: #0054AA;
    --brand-mid: #0677BA;
    --brand-soft: #7BADD7;
    --brand-pale: #CADEEF;
    --brand-mist: #E8F1F8;
    --ink: #1d2430;
    --ink-muted: #3a4452;
    --paper: #ffffff;
    --backdrop: #eef1f4;
  }
  * { box-sizing: border-box; margin: 0; padding: 0; }
  html, body {
    width: 1200px;
    height: 800px;
    overflow: hidden;
    background: var(--backdrop);
    font-family: "Montserrat", sans-serif;
  }
  .sheet {
    width: 1200px;
    height: 800px;
    display: flex;
    align-items: center;
    justify-content: center;
    gap: 60px;
  }
  .card {
    width: 500px;
    height: 286px;
    border-radius: 4px;
    position: relative;
    overflow: hidden;
    box-shadow: 0 10px 30px rgba(20, 40, 70, 0.12);
  }

  /* Front: contact side */
  .card--front {
    background: linear-gradient(120deg, var(--paper) 45%, var(--brand-mist) 100%);
    display: flex;
    align-items: center;
  }
  .front__brand {
    width: 210px;
    display: flex;
    align-items: center;
    justify-content: center;
    gap: 10px;
  }
  .brand-dot {
    width: 22px;
    height: 22px;
    border-radius: 50%;
    background: var(--brand-mid);
  }
  .brand-name {
    font-weight: 500;
    font-size: 20px;
    letter-spacing: 0.18em;
    text-transform: uppercase;
    color: var(--brand-mid);
  }
  .front__divider {
    width: 2px;
    height: 110px;
    background: var(--brand-mid);
  }
  .front__details {
    padding-left: 30px;
  }
  .person__name {
    font-weight: 600;
    font-size: 17px;
    letter-spacing: 0.02em;
    text-transform: uppercase;
    color: var(--ink);
  }
  .person__title {
    font-style: italic;
    font-size: 13px;
    color: var(--ink-muted);
    margin-top: 2px;
  }
  .contact-list {
    list-style: none;
    margin-top: 22px;
  }
  .contact-list li {
    display: flex;
    align-items: center;
    gap: 9px;
    font-size: 12.5px;
    color: var(--ink);
    margin-bottom: 6px;
  }
  .contact-icon {
    width: 18px;
    height: 18px;
    flex: none;
  }

  /* Back: brand side */
  .card--back {
    background: linear-gradient(135deg, var(--brand-deep) 0%, var(--brand-mid) 60%, #2f8fd0 100%);
    display: flex;
    align-items: center;
    justify-content: center;
    gap: 14px;
  }
  .card--back .brand-dot {
    width: 30px;
    height: 30px;
    background: var(--paper);
  }
  .card--back .brand-name {
    font-size: 30px;
    color: var(--paper);
  }
</style>
</head>
<body>
  <main class="sheet">
    <section class="card card--front" aria-label="Business card front">
      <div class="front__brand">
        <span class="brand-dot"></span>
        <span class="brand-name">Vantrel</span>
      </div>
      <div class="front__divider"></div>
      <div class="front__details">
        <p class="person__name">Owen Halvorsen</p>
        <p class="person__title">Founder/CEO</p>
        <ul class="contact-list">
          <li>
            <svg class="contact-icon" viewBox="0 0 18 18" aria-hidden="true">
              <circle cx="9" cy="9" r="9" fill="var(--brand-mid)"/>
              <path d="M6 4.8c.4-.3.9-.2 1.1.2l.8 1.5c.2.4.1.8-.2 1l-.6.5c.4 1 1.2 1.8 2.2 2.3l.5-.6c.3-.3.7-.4 1-.2l1.5.8c.4.2.5.7.2 1.1l-.6.8c-.4.5-1.1.6-1.7.4C8 11.8 6.2 10 5.4 7.7c-.2-.6 0-1.3.4-1.7z" fill="#fff"/>
            </svg>
            555-214-6082
          </li>
          <li>
            <svg class="contact-icon" viewBox="0 0 18 18" aria-hidden="true">
              <circle cx="9" cy="9" r="9" fill="var(--brand-mid)"/>
              <rect x="4.5" y="5.8" width="9" height="6.4" rx="0.8" fill="#fff"/>
              <path d="M4.8 6.2 9 9.3l4.2-3.1" fill="none" stroke="var(--brand-mid)" stroke-width="0.9"/>
            </svg>
            owen@vantrel.co
          </li>
          <li>
            <svg class="contact-icon" viewBox="0 0 18 18" aria-hidden="true">
              <circle cx="9" cy="9" r="9" fill="var(--brand-mid)"/>
              <g fill="none" stroke="#fff" stroke-width="0.9">
                <circle cx="9" cy="9" r="4.4"/>
                <ellipse cx="9" cy="9" rx="1.9" ry="4.4"/>
                <path d="M4.6 9h8.8M5.3 6.8h7.4M5.3 11.2h7.4"/>
              </g>
            </svg>
            www.vantrel.co
          </li>
        </ul>
      </div>
    </section>

    <section class="card card--back" aria-label="Business card back">
      <span class="brand-dot"></span>
      <span class="brand-name">Vantrel</span>
    </section>
  </main>
</body>
</html>
```